Staffing Company Website

We need a website for a new company based out of central California called "Harvest Lane Staffing". We staff truck drivers for agriculture trucking businesses. We don't want a super corporate feel, we want something that feels more inviting to the kind of person who would work in Agriculture/Trucking while still being professional. Please let me know if you have any questions

```html
<!DOCTYPE html>
<html lang="en">
<head>
<meta charset="UTF-8">
<title>Harvest Lane Staffing – Agricultural Trucking Solutions</title>
<link href="https://fonts.googleapis.com/css2?family=Oswald:wght@300;400;500;600;700&family=Poppins:wght@400;500;600&display=swap" rel="stylesheet">
<style>
:root{
  --rust:#B0692A;
  --rust-dark:#9A5A22;
  --olive:#6E8A3C;
  --olive-dark:#5C7631;
  --ink:#2B2B2B;
  --body:#5A5A5A;
  --beige:#F4EDE6;
  --footer:#2A2A2A;
  --white:#FFFFFF;
}
*{margin:0;padding:0;box-sizing:border-box}
html,body{width:1200px;height:4481px;overflow:hidden}
body{position:relative;background:var(--white);font-family:'Poppins',sans-serif;color:var(--body)}
.abs{position:absolute}
.heading{font-family:'Oswald',sans-serif;font-weight:600;color:var(--ink);text-transform:uppercase;letter-spacing:.5px}
.btn{position:absolute;display:flex;align-items:center;justify-content:center;font-family:'Poppins',sans-serif;font-weight:600;font-size:11px;text-transform:uppercase;color:var(--white);border-radius:2px}
.btn-olive{background:var(--olive)}
.btn-rust{background:var(--rust)}
.photo{position:absolute;overflow:hidden}

/* hero */
.hero{position:absolute;left:0;top:0;width:1200px;height:593px;background:var(--rust)}
.hero-cut{position:absolute;left:0;top:0;width:1200px;height:593px;background:var(--white);clip-path:polygon(500px 0,1200px 0,1200px 593px,710px 593px)}
.hero-photo{position:absolute;left:0;top:0;width:1200px;height:593px;background:linear-gradient(160deg,#C7D8E6 0%,#9DB6C7 30%,#4F6F3A 60%,#3C4A36 100%);clip-path:polygon(522px 0,1200px 0,1200px 593px,735px 593px)}
.brand{position:absolute;display:flex;align-items:center;gap:12px}
.brand-mark{width:46px;height:46px;border-radius:50%;background:var(--white);opacity:.95}
.brand-name{font-family:'Poppins',sans-serif;font-weight:500;color:var(--white);text-transform:uppercase;line-height:1.15}
.nav{position:absolute;left:575px;top:34px;display:flex;gap:18px;align-items:center;font-size:11.5px;font-weight:500;color:var(--ink);text-transform:uppercase}
.nav-home{width:12px;height:12px}
.hero-kicker{left:89px;top:166px;font-family:'Oswald',sans-serif;font-weight:500;font-size:21px;color:var(--white);text-transform:uppercase}
.hero-title{left:87px;top:198px;font-family:'Oswald',sans-serif;font-weight:700;font-size:64px;line-height:62px;color:var(--white);text-transform:uppercase}
.hero-sub{left:89px;top:400px;width:400px;font-size:15px;line-height:19px;color:var(--white)}
.hero-btn{left:89px;top:456px;width:148px;height:38px;background:var(--white);color:var(--ink)}

.intro{left:200px;top:666px;width:800px;text-align:center;font-family:'Oswald',sans-serif;font-weight:300;font-size:22.5px;line-height:36px;color:var(--ink);text-transform:uppercase}

/* who we are */
.blob-green{left:-180px;top:830px;width:560px;height:560px;background:var(--olive);border-radius:110px;transform:rotate(45deg)}
.blob-beige{border-radius:90px;background:var(--beige);transform:rotate(45deg)}
.who-photo{left:144px;top:838px;width:420px;height:470px;border-radius:0 0 80px 0;background:linear-gradient(180deg,#A9C3DA 0%,#D9E2E8 35%,#8C8F86 60%,#3E5A7C 100%)}
.who-title{left:626px;top:872px;font-size:40px}
.who-text{left:626px;top:938px;width:445px;font-size:13.2px;line-height:22px}
.who-btn{left:626px;top:1202px;width:122px;height:38px}

/* how it works */
.how-title{left:0;top:1424px;width:1200px;text-align:center;font-size:40px}
.step{position:absolute;top:1500px;width:246px;height:366px;background:var(--white);border-radius:8px;box-shadow:0 6px 20px rgba(0,0,0,.09);overflow:hidden}
.step-photo{height:205px}
.step-body{padding:20px 22px 0 25px;position:relative}
.step-body::before{content:"";position:absolute;left:0;top:20px;width:3px;height:20px;background:var(--rust)}
.step-name{font-family:'Oswald',sans-serif;font-weight:500;font-size:15.5px;color:var(--ink);text-transform:uppercase}
.step-text{margin-top:10px;font-size:12px;line-height:18px}
.step-link{margin-top:8px;font-size:11px;font-weight:600;color:var(--ink);text-decoration:underline;text-transform:uppercase}
.how-book{left:427px;top:1894px;width:150px;height:37px}
.how-quote{left:584px;top:1894px;width:189px;height:37px}

/* impact */
.impact-title{left:0;top:2000px;width:1200px;text-align:center;font-size:40px}
.slide{position:absolute;top:2078px;height:447px;border-radius:14px;overflow:hidden}
.slide-caption{position:absolute;left:0;bottom:42px;width:100%;text-align:center;font-family:'Oswald',sans-serif;font-weight:500;font-size:22px;color:var(--white);text-transform:uppercase;text-decoration:underline;text-underline-offset:5px}
.slide-arrow{position:absolute;right:30px;bottom:30px;width:58px;height:58px;border-radius:50%;background:var(--white);display:flex;align-items:center;justify-content:center}

/* unique value */
.value-title{left:188px;top:2685px;font-size:40px}
.value-text{left:189px;top:2750px;width:420px;font-size:14px;line-height:22px}
.value-list{left:189px;top:2824px;list-style:none;font-size:13.5px;font-weight:500;color:#3A3A3A}
.value-list li{margin-bottom:14px;padding-left:13px;position:relative}
.value-list li::before{content:"";position:absolute;left:0;top:8px;width:5px;height:5px;border-radius:50%;background:var(--olive)}
.value-btn{left:189px;top:2939px;width:167px;height:38px}
.value-photo{left:682px;top:2631px;width:328px;height:367px;border-radius:40px 0 60px 0;background:linear-gradient(180deg,#5F7F40 0%,#8EA663 45%,#A8473E 70%,#55688A 100%)}

/* pricing */
.cost-title{left:0;top:3072px;width:1200px;text-align:center;font-size:40px}
.cost-sub{left:0;top:3137px;width:1200px;text-align:center;font-size:15px;color:var(--body)}
.plan{position:absolute;background:var(--white);border-radius:14px;box-shadow:0 6px 22px rgba(0,0,0,.08);padding:22px 14px 0;text-align:center}
.plan-featured{border:2px solid #C8D2B4;box-shadow:0 10px 28px rgba(0,0,0,.12)}
.plan-name{font-family:'Oswald',sans-serif;font-weight:500;font-size:16px;color:var(--ink)}
.plan-price{margin-top:4px;font-family:'Oswald',sans-serif;font-weight:600;font-size:36px;color:var(--rust)}
.plan-price small{font-size:12px;font-weight:500;color:var(--ink)}
.plan-tag{margin-top:10px;font-family:'Oswald',sans-serif;font-size:11.5px;color:var(--ink);text-transform:uppercase}
.plan-rows{margin:16px 4px 0;text-align:left;font-size:9.5px}
.plan-row{display:flex;justify-content:space-between;margin-bottom:9px;color:#444}
.plan-row span:last-child{color:var(--rust);font-weight:500}
.plan-rule{height:1px;background:#DDD;margin:14px 0 12px}
.plan-feat{text-align:left;list-style:none;font-size:10.5px;color:#444;padding:0 4px}
.plan-feat li{display:flex;align-items:center;gap:7px;margin-bottom:11px}
.tick{width:11px;height:11px;flex:none}
.plan-btn{position:absolute;left:14px;right:14px;height:35px}
.plan-featured .plan-btn{height:38px}

/* cta and footer */
.footer-bg{left:0;top:0;width:1200px;height:4481px}
.cta{left:158px;top:3768px;width:884px;height:192px;background:var(--olive);border-radius:24px}
.cta-title{left:218px;top:3806px;font-family:'Oswald',sans-serif;font-weight:700;font-size:46px;color:var(--white);text-transform:uppercase;letter-spacing:.5px}
.cta-text{left:218px;top:3872px;width:560px;font-family:'Oswald',sans-serif;font-weight:500;font-size:17px;line-height:22px;color:var(--white);text-transform:uppercase}
.cta-btn{left:848px;top:3846px;width:132px;height:40px;background:var(--white);color:var(--ink);font-size:12px}
.foot-brand{left:108px;top:4139px}
.foot-brand .brand-mark{width:70px;height:70px}
.foot-brand .brand-name{font-size:23px;border-left:2px solid var(--white);padding-left:14px}
.socials{left:124px;top:4246px;display:flex;gap:10px}
.social{width:44px;height:44px;border-radius:50%;background:#3D3D3D}
.foot-col{top:4082px;color:var(--white)}
.foot-head{font-family:'Oswald',sans-serif;font-weight:500;font-size:18px;text-transform:uppercase;margin-bottom:22px}
.foot-list{list-style:none;font-size:13px;line-height:17px}
.foot-list li{margin-bottom:17px}
.foot-list li::before{content:"› ";}
.contact-item{display:flex;gap:10px;font-size:13px;line-height:18px;margin-bottom:16px}
.contact-item svg{flex:none;margin-top:2px}
.foot-rule{left:0;top:4417px;width:1200px;height:1px;background:#444}
.copyright{left:0;top:4445px;width:1200px;text-align:center;font-size:13px;color:var(--white)}
.to-top{left:1132px;top:4401px;width:40px;height:40px;border-radius:50%;background:var(--olive);display:flex;align-items:center;justify-content:center}
</style>
</head>
<body>

<!-- hero -->
<section class="hero">
  <div class="hero-cut"></div>
  <div class="hero-photo" role="img" aria-label="Green farm tractor hauling a loaded trailer on a rural highway"></div>
</section>
<div class="brand" style="left:89px;top:26px">
  <div class="brand-mark"></div>
  <div class="brand-name" style="font-size:14px">Harvest Lane<br>Staffing</div>
</div>
<nav class="nav">
  <svg class="nav-home" viewBox="0 0 12 12"><path d="M6 1L1 5.5h1.5V11h3V8h1v3h3V5.5H11z" fill="#6E8A3C"/></svg>
  <span>About Us</span><span>Services</span><span>Career</span><span>Pricing</span><span>Contact Us</span>
</nav>
<div class="btn btn-olive" style="left:993px;top:24px;width:117px;height:37px">Book Now</div>
<div class="abs hero-kicker">Welcome to Harvest Lane Staffing</div>
<h1 class="abs hero-title">Agricultural<br>Trucking<br>Solutions</h1>
<p class="abs hero-sub">providing skilled truck drivers for Central California's agricultural trucking industry</p>
<div class="btn hero-btn">Get an Estimate</div>

<p class="abs intro">We understand the unique demands of agriculture and trucking, and we're here to connect businesses with reliable, experienced drivers who keep the wheels of progress moving.</p>

<!-- who we are -->
<div class="abs blob-green"></div>
<div class="abs blob-beige" style="left:960px;top:1160px;width:330px;height:330px"></div>
<div class="photo who-photo" role="img" aria-label="Farmer in a straw hat holding a tablet beside a green tractor"></div>
<h2 class="abs heading who-title">Who We Are</h2>
<p class="abs who-text">At Harvest Lane Staffing, we pride ourselves on being more than just a staffing agency. Based in the heart of Central California, we specialize in providing experienced truck drivers to the agricultural trucking industry. With deep roots in agriculture and transportation, our team understands the unique needs of both drivers and businesses. Our goal is to create lasting partnerships, placing skilled professionals in roles where they can succeed and grow.<br>With deep roots in agriculture and transportation, our team understands the unique needs of both drivers and businesses. Our goal is to create lasting</p>
<div class="btn btn-olive who-btn">Read More</div>

<!-- how it works -->
<h2 class="abs heading how-title">How Harvest Lane Works</h2>
<article class="step" style="left:89px">
  <div class="step-photo" style="background:linear-gradient(180deg,#B9C2C4,#6F7F4A 55%,#4E6236)" role="img" aria-label="Farm workers loading a trailer in a field"></div>
  <div class="step-body"><div class="step-name">Tailored Staffing</div><p class="step-text">We provide qualified, experienced truck drivers for businesses throughout...</p><div class="step-link">Read More</div></div>
</article>
<article class="step" style="left:348px">
  <div class="step-photo" style="background:linear-gradient(180deg,#C4C9C8,#7C6F55 55%,#4E4A3A)" role="img" aria-label="Two drivers walking across a farm field"></div>
  <div class="step-body"><div class="step-name">Driver Recruitment</div><p class="step-text">We carefully vet and select drivers who meet the highest standards of safety...</p><div class="step-link">Read More</div></div>
</article>
<article class="step" style="left:607px">
  <div class="step-photo" style="background:linear-gradient(180deg,#B5CBE0,#4E8A3A 55%,#2F5A2A)" role="img" aria-label="Workers on a green harvester"></div>
  <div class="step-body"><div class="step-name">Ongoing Support</div><p class="step-text">We don't just place drivers; we support them throughout their employment journey...</p><div class="step-link">Read More</div></div>
</article>
<article class="step" style="left:866px">
  <div class="step-photo" style="background:linear-gradient(180deg,#C9D6E2,#7A8C62 55%,#5A6650)" role="img" aria-label="Tractor pulling hay bales along a road"></div>
  <div class="step-body"><div class="step-name">We Pick It Back Up</div><p class="step-text">We don't just place drivers; we support them throughout their employment journey...</p><div class="step-link">Read More</div></div>
</article>
<div class="btn btn-rust how-book">Book Online</div>
<div class="btn btn-olive how-quote">Request a Quote</div>

<!-- impact -->
<h2 class="abs heading impact-title">Our Impact</h2>
<div class="slide" style="left:-20px;width:229px;background:linear-gradient(180deg,#8C9A6A,#A29457 60%,#6E6A3A)" role="img" aria-label="Green combine harvester in a field"></div>
<div class="slide" style="left:228px;width:742px;background:linear-gradient(180deg,#A9B3A2 0%,#8A8F78 35%,#6C7B45 70%,#4E6A2E 100%)" role="img" aria-label="Red tractor working a planted field">
  <div class="slide-caption">Landscaping and Planting</div>
  <div class="slide-arrow"><svg width="20" height="14" viewBox="0 0 20 14"><path d="M1 7h17M12 1l6 6-6 6" stroke="#2B2B2B" stroke-width="1.6" fill="none"/></svg></div>
</div>
<div class="slide" style="left:988px;width:232px;background:linear-gradient(180deg,#C9B27A,#B99B5A 60%,#9E7E3E)" role="img" aria-label="Combine harvesting a wheat field"></div>

<!-- unique value -->
<div class="abs blob-beige" style="left:-210px;top:2970px;width:330px;height:330px"></div>
<h2 class="abs heading value-title">Our Unique Value</h2>
<p class="abs value-text">we focus on your specific needs in the agricultural trucking sector. Our dedication to exceptional service and skilled drivers ensures smooth and efficient operations</p>
<ul class="abs value-list">
  <li>Deep understanding of the agricultural trucking industry.</li>
  <li>Personalized service tailored to your specific needs.</li>
  <li>Experienced, reliable, and safety-focused drivers.</li>
</ul>
<div class="btn btn-olive value-btn">Request Staffing</div>
<div class="photo value-photo" role="img" aria-label="Smiling farm worker in a plaid shirt standing in front of a tractor"></div>

<!-- pricing -->
<h2 class="abs heading cost-title">Cost &amp; Service</h2>
<p class="abs cost-sub">Whether you want to get organized, keep your personal life on track</p>

<div class="plan" style="left:163px;top:3208px;width:270px;height:458px">
  <div class="plan-name">ESSENTIAL</div>
  <div class="plan-price">$1,500<small>/Month</small></div>
  <div class="plan-tag">Capture ideas and find them quickly</div>
  <div class="plan-rows">
    <div class="plan-row"><span>Hiring need:</span><span>1–10 drivers/month</span></div>
    <div class="plan-row"><span>Fleet size:</span><span>1–100 trucks</span></div>
    <div class="plan-row"><span>Number of recruiters:</span><span>1+</span></div>
    <div class="plan-row"><span>Monthly ad budget:</span><span>$2,000/month</span></div>
  </div>
  <div class="plan-rule"></div>
  <ul class="plan-feat">
    <li><svg class="tick" viewBox="0 0 11 11"><circle cx="5.5" cy="5.5" r="5.5" fill="#B0692A"/><path d="M3 5.6l1.7 1.7L8 4" stroke="#fff" stroke-width="1.3" fill="none"/></svg>Social media ads management</li>
    <li><svg class="tick" viewBox="0 0 11 11"><circle cx="5.5" cy="5.5" r="5.5" fill="#B0692A"/><path d="M3 5.6l1.7 1.7L8 4" stroke="#fff" stroke-width="1.3" fill="none"/></svg>ATS integration</li>
    <li><svg class="tick" viewBox="0 0 11 11"><circle cx="5.5" cy="5.5" r="5.5" fill="#B0692A"/><path d="M3 5.6l1.7 1.7L8 4" stroke="#fff" stroke-width="1.3" fill="none"/></svg>Automated instant driver follow-ups</li>
    <li><svg class="tick" viewBox="0 0 11 11"><circle cx="5.5" cy="5.5" r="5.5" fill="#B0692A"/><path d="M3 5.6l1.7 1.7L8 4" stroke="#fff" stroke-width="1.3" fill="none"/></svg>Weekly reporting and accountability</li>
  </ul>
  <div class="btn btn-rust plan-btn" style="top:388px">Get Started</div>
</div>

<div class="plan plan-featured" style="left:454px;top:3191px;width:290px;height:490px">
  <div class="plan-name">BASIC</div>
  <div class="plan-price">$2,500<small>/Month</small></div>
  <div class="plan-tag">Capture ideas and find them quickly</div>
  <div class="plan-rows">
    <div class="plan-row"><span>Hiring need:</span><span style="color:#6E8A3C">10–20 drivers/month</span></div>
    <div class="plan-row"><span>Fleet size:</span><span style="color:#6E8A3C">100–250 trucks</span></div>
    <div class="plan-row"><span>Number of recruiters:</span><span style="color:#6E8A3C">2+</span></div>
    <div class="plan-row"><span>Monthly ad budget:</span><span style="color:#6E8A3C">$5,000/month</span></div>
  </div>
  <div class="plan-rule"></div>
  <ul class="plan-feat">
    <li><svg class="tick" viewBox="0 0 11 11"><circle cx="5.5" cy="5.5" r="5.5" fill="#6E8A3C"/><path d="M3 5.6l1.7 1.7L8 4" stroke="#fff" stroke-width="1.3" fill="none"/></svg>Social media ads management</li>
    <li><svg class="tick" viewBox="0 0 11 11"><circle cx="5.5" cy="5.5" r="5.5" fill="#6E8A3C"/><path d="M3 5.6l1.7 1.7L8 4" stroke="#fff" stroke-width="1.3" fill="none"/></svg>ATS integration</li>
    <li><svg class="tick" viewBox="0 0 11 11"><circle cx="5.5" cy="5.5" r="5.5" fill="#6E8A3C"/><path d="M3 5.6l1.7 1.7L8 4" stroke="#fff" stroke-width="1.3" fill="none"/></svg>Automated instant driver follow-ups</li>
    <li><svg class="tick" viewBox="0 0 11 11"><circle cx="5.5" cy="5.5" r="5.5" fill="#6E8A3C"/><path d="M3 5.6l1.7 1.7L8 4" stroke="#fff" stroke-width="1.3" fill="none"/></svg>Weekly reporting and accountability</li>
  </ul>
  <div class="btn btn-olive plan-btn" style="top:416px">Get Started</div>
</div>

<div class="plan" style="left:765px;top:3208px;width:270px;height:458px">
  <div class="plan-name">ADVANCED</div>
  <div class="plan-price">$6,000<small>/Month</small></div>
  <div class="plan-tag">Capture ideas and find them quickly</div>
  <div class="plan-rows">
    <div class="plan-row"><span>Hiring need:</span><span>20–30 drivers/month</span></div>
    <div class="plan-row"><span>Fleet size:</span><span>250–500 trucks</span></div>
    <div class="plan-row"><span>Number of recruiters:</span><span>3+</span></div>
    <div class="plan-row"><span>Monthly ad budget:</span><span>$20,000/month</span></div>
  </div>
  <div class="plan-rule"></div>
  <ul class="plan-feat">
    <li><svg class="tick" viewBox="0 0 11 11"><circle cx="5.5" cy="5.5" r="5.5" fill="#B0692A"/><path d="M3 5.6l1.7 1.7L8 4" stroke="#fff" stroke-width="1.3" fill="none"/></svg>Social media ads management</li>
    <li><svg class="tick" viewBox="0 0 11 11"><circle cx="5.5" cy="5.5" r="5.5" fill="#B0692A"/><path d="M3 5.6l1.7 1.7L8 4" stroke="#fff" stroke-width="1.3" fill="none"/></svg>ATS integration</li>
    <li><svg class="tick" viewBox="0 0 11 11"><circle cx="5.5" cy="5.5" r="5.5" fill="#B0692A"/><path d="M3 5.6l1.7 1.7L8 4" stroke="#fff" stroke-width="1.3" fill="none"/></svg>Automated instant driver follow-ups</li>
    <li><svg class="tick" viewBox="0 0 11 11"><circle cx="5.5" cy="5.5" r="5.5" fill="#B0692A"/><path d="M3 5.6l1.7 1.7L8 4" stroke="#fff" stroke-width="1.3" fill="none"/></svg>Weekly reporting and accountability</li>
  </ul>
  <div class="btn btn-rust plan-btn" style="top:388px">Get Started</div>
</div>

<!-- footer and call to action -->
<svg class="abs footer-bg" viewBox="0 0 1200 4481" style="pointer-events:none">
  <path d="M0 4060 C 400 4050 760 4020 960 3940 C 1080 3890 1130 3820 1200 3815 L1200 4481 L0 4481 Z" fill="#2A2A2A"/>
</svg>
<div class="abs cta"></div>
<div class="abs cta-title">Ready to Drive With Us?</div>
<p class="abs cta-text">Join our team of experienced drivers and enjoy the support you deserve. Start your journey today and become part</p>
<div class="btn cta-btn">Apply Now</div>

<div class="brand foot-brand">
  <div class="brand-mark"></div>
  <div class="brand-name">Harvest<br>Lane<br>Staffing</div>
</div>
<div class="abs socials">
  <div class="social" aria-label="Social profile"></div>
  <div class="social" aria-label="Social profile"></div>
  <div class="social" aria-label="Social profile"></div>
  <div class="social" aria-label="Social profile"></div>
</div>

<div class="abs foot-col" style="left:439px">
  <div class="foot-head">Quick Links</div>
  <ul class="foot-list"><li>Home</li><li>About us</li><li>Services</li><li>Career</li><li>Pricing</li><li>Contact Us</li></ul>
</div>
<div class="abs foot-col" style="left:634px">
  <div class="foot-head">Services</div>
  <ul class="foot-list"><li>Tailored Staffing</li><li>Driver Recruitment</li><li>Ongoing Support</li><li>We Pick It Back Up</li></ul>
</div>
<div class="abs foot-col" style="left:856px;width:260px">
  <div class="foot-head">Contact Info</div>
  <div class="contact-item"><svg width="14" height="11" viewBox="0 0 14 11"><rect x=".5" y=".5" width="13" height="10" rx="1" fill="none" stroke="#fff"/><path d="M1 1l6 5 6-5" stroke="#fff" fill="none"/></svg><span>Email:<br>info@harvestlanestaffing.com</span></div>
  <div class="contact-item"><svg width="14" height="14" viewBox="0 0 14 14"><path d="M3 1l2.5 3-1.5 1.5c.8 1.8 2.2 3.2 4 4L9.5 8l3 2.5-1.5 2.5C6 13 1 8 1 2.5z" fill="#fff"/></svg><span>Phone:<br>(559) 014-2260</span></div>
  <div class="contact-item"><svg width="12" height="15" viewBox="0 0 12 15"><path d="M6 0a6 6 0 0 0-6 6c0 4.5 6 9 6 9s6-4.5 6-9a6 6 0 0 0-6-6z" fill="#fff"/><circle cx="6" cy="6" r="2.2" fill="#2A2A2A"/></svg><span>Location:<br>48 Orchard Road, Fresno,<br>CA 93721</span></div>
</div>

<div class="abs foot-rule"></div>
<div class="abs to-top"><svg width="14" height="10" viewBox="0 0 14 10"><path d="M1 8l6-6 6 6" stroke="#fff" stroke-width="2" fill="none"/></svg></div>
<p class="abs copyright">©Copyright 2024 Harvest Lane Staffing | All Rights Reserved</p>

</body>
</html>
```